I need a simple infographic that describes the 4 basic elements of how to effectively create change.

The overall title (Gentle Pressure Relentlessly Applied) should be at the top of the infographic. Subtitle is: "Leading Change".
There are four steps:
1. Alignment- Agreement on Approach
2. Transparency- Metrics for Assurance
3. Skills- Training and Coaching
4. Integrity- Culture of Accountability

Target Market(s)

Business Leaders in a training workshop

Font styles to use
Serif

Requirements
Must have
• Here are the 4 elements of the Infographic: Please show them in order.
• 1. Agreement on Approach. (Alignment)
• 2. Metrics for Assurance (Transparency)
• 3. Training and Coaching (Skills)
• 4. Culture of Accountability (Integrity)
Nice to have
• Cool Graphics that depict the 4 steps.
Should not have
• Pictures.

```html
<!DOCTYPE html>
<html lang="en">
<head>
<meta charset="utf-8">
<title>Gentle Pressure Relentlessly Applied – Leading Change</title>
<link rel="stylesheet" href="https://fonts.googleapis.com/css2?family=Bodoni+Moda:wght@500&family=Raleway:wght@400;500&family=Gochi+Hand&display=swap">
<style>
  :root {
    --paper: #ffffff;
    --ink: #111111;
    --blue-deep: #0f7ee9;
    --blue-mid: #3d9ef0;
    --blue-light: #86c7fb;
    --number-stroke: #2f8fef;
    --label: #ffffff;
  }
  html, body {
    margin: 0;
    padding: 0;
    overflow: hidden;
    background: var(--paper);
  }
  .canvas {
    position: relative;
    width: 1200px;
    height: 884px;
    background: var(--paper);
    overflow: hidden;
  }
  .heading {
    position: absolute;
    top: 36px;
    left: 0;
    width: 100%;
    margin: 0;
    text-align: center;
    font-family: "Bodoni Moda", "Didot", serif;
    font-weight: 500;
    font-size: 41px;
    line-height: 1.12;
    letter-spacing: -0.5px;
    color: var(--ink);
  }
  .heading .subtitle { display: block; }
  .puzzle {
    position: absolute;
    left: 0;
    top: 0;
  }
  .step-name, .step-note {
    font-family: "Raleway", sans-serif;
    fill: var(--label);
    text-anchor: middle;
  }
  .step-name { font-weight: 400; }
  .step-note { font-weight: 500; font-size: 18px; }
  .step-number {
    font-family: "Gochi Hand", cursive;
    font-size: 112px;
    fill: none;
    stroke: var(--number-stroke);
    stroke-width: 3;
    text-anchor: middle;
  }
</style>
</head>
<body>
<main class="canvas">
  <h1 class="heading">Gentle Pressure Relentlessly Applied<span class="subtitle">Leading Change</span></h1>

  <svg class="puzzle" width="1200" height="884" viewBox="0 0 1200 884" aria-label="Four steps of leading change">
    <defs>
      <clipPath id="disc-clip"><circle cx="0" cy="0" r="300"/></clipPath>
      <linearGradient id="fill-alignment" gradientUnits="userSpaceOnUse" x1="-300" y1="-300" x2="0" y2="0">
        <stop offset="0" stop-color="#3a9cf0"/><stop offset="1" stop-color="#8ccafb"/>
      </linearGradient>
      <linearGradient id="fill-transparency" gradientUnits="userSpaceOnUse" x1="0" y1="-300" x2="300" y2="0">
        <stop offset="0" stop-color="#0f7ee9"/><stop offset="1" stop-color="#74c0fb"/>
      </linearGradient>
      <linearGradient id="fill-skills" gradientUnits="userSpaceOnUse" x1="-300" y1="0" x2="0" y2="300">
        <stop offset="0" stop-color="#1583ec"/><stop offset="1" stop-color="#84c6fb"/>
      </linearGradient>
      <linearGradient id="fill-integrity" gradientUnits="userSpaceOnUse" x1="0" y1="0" x2="300" y2="300">
        <stop offset="0" stop-color="#0c7be8"/><stop offset="1" stop-color="#74c0fb"/>
      </linearGradient>
      <radialGradient id="badge-fill" cx="0.45" cy="0.35" r="0.7">
        <stop offset="0.6" stop-color="#ffffff"/><stop offset="1" stop-color="#e6e8ec"/>
      </radialGradient>
      <filter id="badge-shadow" x="-40%" y="-40%" width="180%" height="180%">
        <feDropShadow dx="0" dy="10" stdDeviation="9" flood-color="#000" flood-opacity="0.28"/>
      </filter>
    </defs>

    <g class="puzzle-disc" transform="translate(600 492)">
      <g clip-path="url(#disc-clip)">
        <rect class="piece-alignment" x="-300" y="-300" width="300" height="300" fill="url(#fill-alignment)"/>
        <rect class="piece-transparency" x="0" y="-300" width="300" height="300" fill="url(#fill-transparency)"/>
        <rect class="piece-skills" x="-300" y="0" width="300" height="300" fill="url(#fill-skills)"/>
        <rect class="piece-integrity" x="0" y="0" width="300" height="300" fill="url(#fill-integrity)"/>
        <rect class="seam" x="-7" y="-310" width="14" height="620" fill="var(--paper)"/>
        <rect class="seam" x="-310" y="-7" width="620" height="14" fill="var(--paper)"/>
      </g>

      <g class="tab">
        <circle cx="30" cy="-190" r="28" fill="url(#fill-alignment)" stroke="var(--paper)" stroke-width="8"/>
        <rect x="-8" y="-204" width="22" height="28" fill="url(#fill-alignment)"/>
      </g>
      <g class="tab">
        <circle cx="125" cy="-28" r="28" fill="url(#fill-integrity)" stroke="var(--paper)" stroke-width="8"/>
        <rect x="111" y="-12" width="28" height="20" fill="url(#fill-integrity)"/>
      </g>
      <g class="tab">
        <circle cx="-158" cy="27" r="27" fill="url(#fill-alignment)" stroke="var(--paper)" stroke-width="8"/>
        <rect x="-172" y="-8" width="28" height="20" fill="url(#fill-alignment)"/>
      </g>
      <g class="tab">
        <circle cx="-30" cy="170" r="28" fill="url(#fill-integrity)" stroke="var(--paper)" stroke-width="8"/>
        <rect x="-14" y="156" width="22" height="28" fill="url(#fill-integrity)"/>
      </g>

      <text class="step-name" x="-152" y="-78" font-size="44">Alignment</text>
      <text class="step-note" x="-152" y="-48">Agreement on Approach</text>

      <text class="step-name" x="142" y="-104" font-size="36">Transparency</text>
      <text class="step-note" x="142" y="-78">Metrics for Assurance</text>

      <text class="step-name" x="-136" y="108" font-size="62">Skills</text>
      <text class="step-note" x="-136" y="136">Training and Coaching</text>

      <text class="step-name" x="158" y="56" font-size="50">Integrity</text>
      <text class="step-note" x="158" y="84">Culture of Accountability</text>

      <g class="badge" filter="url(#badge-shadow)">
        <circle cx="-165" cy="-218" r="80" fill="url(#badge-fill)"/>
        <circle cx="160" cy="-228" r="80" fill="url(#badge-fill)"/>
        <circle cx="-124" cy="250" r="80" fill="url(#badge-fill)"/>
        <circle cx="205" cy="232" r="80" fill="url(#badge-fill)"/>
      </g>
      <text class="step-number" x="-165" y="-180">1</text>
      <text class="step-number" x="160" y="-190">2</text>
      <text class="step-number" x="-124" y="288">3</text>
      <text class="step-number" x="205" y="270">4</text>
    </g>
  </svg>
</main>
</body>
</html>
```